Design for an iOS and Android app managing shopping list

The app allows you to keep manage shopping lists, each shopping list being made of items to buy...
We need a design for the 3 screens of the app:
a) global view showing list of (shopping) list
b) form enabling to edit the name of a (shopping) list
c) detailed view listing the contents/items of a (shopping) list
d) 1 text page [not illustrated]
2 "alerts" items are also to be designed: confirm and error pop ups.
No specific guidelines, nor logo or whatever.
It will be a free app distributed on iOS and Androïd.
We just want to make it looking nice & very usable for end users.

```html
<!DOCTYPE html>
<html lang="en">
<head>
<meta charset="utf-8">
<title>Shopping lists – drawer</title>
<link rel="stylesheet" href="https://fonts.googleapis.com/css2?family=Lato:wght@300;400;700&display=swap">
<style>
:root{
  --status-bg:#2a343a;
  --drawer-bg:#26323a;
  --header-bg:#2b373e;
  --app-bg:#1d2529;
  --app-bar:#2c383f;
  --teal:#12403c;
  --text-light:#ffffff;
  --text-muted:#c9d0d4;
  --badge:#ef5b5b;
  --home-a:#8aa1ae;
  --home-b:#b9c8cf;
  --party-a:#5a5470;
  --party-b:#8e6877;
  --grocery-a:#a38b7c;
  --grocery-b:#dcc8b6;
}
*{box-sizing:border-box;margin:0;padding:0}
html,body{width:750px;height:1200px;overflow:hidden}
body{background:var(--app-bg);font-family:"Lato",sans-serif;color:var(--text-light);position:relative}

.status-bar{position:absolute;left:0;top:0;width:750px;height:56px;background:var(--status-bg);display:flex;align-items:center;justify-content:flex-end;gap:14px;padding-right:22px;z-index:3}
.status-time{font-size:30px;font-weight:400}

.app-behind{position:absolute;left:0;top:56px;width:750px;height:1144px;background:var(--app-bg)}
.app-toolbar{position:absolute;left:0;top:0;width:750px;height:285px;background:var(--app-bar)}
.chat-icon{position:absolute;left:685px;top:48px}
.app-field{position:absolute;left:665px;top:150px;width:60px;height:100px;background:#6b6f72;border-radius:3px}
.app-chevron{position:absolute;left:680px;top:655px}
.app-tile{position:absolute;left:665px;width:65px;background:var(--teal)}

.drawer{position:absolute;left:0;top:56px;width:665px;height:1144px;background:var(--drawer-bg);z-index:2;box-shadow:4px 0 10px rgba(0,0,0,.35)}
.profile{height:306px;background:var(--header-bg);padding:40px 35px 0}
.profile-photo{width:146px;height:146px;border-radius:50%;border:5px solid #fff;background:linear-gradient(160deg,#e8e4df,#b89a84)}
.profile-name{margin-top:42px;font-size:26px;font-weight:700;color:var(--text-muted)}
.profile-email{margin-top:4px;font-size:27px;font-weight:400;color:var(--text-muted)}

.list-card{position:relative;height:252px;padding:28px 35px 0;overflow:hidden}
.list-card--home{background:linear-gradient(90deg,var(--home-a),var(--home-b))}
.list-card--party{background:linear-gradient(90deg,var(--party-a),var(--party-b))}
.list-card--grocery{background:linear-gradient(90deg,var(--grocery-a),var(--grocery-b))}
.list-scene{position:absolute;right:0;bottom:0;width:300px;height:190px;border-top-left-radius:60px}
.list-card--home .list-scene{background:linear-gradient(180deg,rgba(255,255,255,.08),rgba(240,232,215,.55))}
.list-card--party .list-scene{background:linear-gradient(180deg,rgba(255,220,170,.08),rgba(50,40,60,.55))}
.list-card--grocery .list-scene{background:linear-gradient(180deg,rgba(255,255,255,.1),rgba(230,90,70,.35))}
.list-title{position:relative;font-size:58px;font-weight:400;line-height:1.05}
.list-count{position:relative;display:inline-block;margin-top:10px;background:var(--badge);font-size:27px;padding:3px 10px;border-radius:2px}
.list-members{position:relative;display:flex;gap:8px;margin-top:28px}
.member{width:66px;height:66px;border-radius:50%;border:3px solid #fff}
.member--a{background:linear-gradient(160deg,#e6dfd8,#a58470)}
.member--b{background:linear-gradient(160deg,#d9dde0,#8a7a6c)}
.member--c{background:linear-gradient(160deg,#d8c7a6,#6d5a45)}
.member--d{background:linear-gradient(160deg,#6c7a4e,#3a2a20)}

.create-list{display:flex;align-items:center;height:90px;padding-left:40px;color:var(--text-muted)}
.create-plus{font-size:44px;font-weight:300;width:110px}
.create-label{font-size:36px;font-weight:300}
</style>
</head>
<body>
<header class="status-bar">
  <svg width="38" height="30" viewBox="0 0 38 30" aria-label="3G signal">
    <text x="0" y="11" font-family="Lato, sans-serif" font-size="12" font-weight="700" fill="#fff">3G</text>
    <polygon points="36,2 36,28 10,28" fill="#fff"/>
  </svg>
  <svg width="20" height="32" viewBox="0 0 20 32" aria-label="Battery charging">
    <rect x="6" y="0" width="8" height="4" fill="#fff"/>
    <rect x="1" y="4" width="18" height="28" fill="#fff"/>
    <polygon points="11,9 5,20 10,20 8,28 15,16 10,16" fill="var(--status-bg)"/>
  </svg>
  <span class="status-time">7:50</span>
</header>

<div class="app-behind" aria-hidden="true">
  <div class="app-toolbar">
    <svg class="chat-icon" width="44" height="40" viewBox="0 0 44 40">
      <path d="M4 2h36a3 3 0 0 1 3 3v22a3 3 0 0 1-3 3H14l-10 9v-9a3 3 0 0 1-3-3V5a3 3 0 0 1 3-3z" fill="#6f7a80"/>
      <circle cx="14" cy="16" r="2.5" fill="#2c383f"/><circle cx="22" cy="16" r="2.5" fill="#2c383f"/><circle cx="30" cy="16" r="2.5" fill="#2c383f"/>
    </svg>
    <div class="app-field"></div>
  </div>
  <svg class="app-chevron" width="30" height="20" viewBox="0 0 30 20"><path d="M3 17L15 5l12 12" stroke="#4a555b" stroke-width="4" fill="none"/></svg>
  <div class="app-tile" style="top:740px;height:225px"></div>
  <div class="app-tile" style="top:972px;height:225px"></div>
</div>

<nav class="drawer">
  <section class="profile">
    <div class="profile-photo" role="img" aria-label="Profile photo of Lena"></div>
    <p class="profile-name">Lena</p>
    <p class="profile-email">lena@listly.app</p>
  </section>

  <article class="list-card list-card--home">
    <div class="list-scene" role="img" aria-label="Illustration of a kitchen with a grocery bag on a table"></div>
    <h2 class="list-title">Home</h2>
    <span class="list-count">2 items</span>
    <div class="list-members">
      <span class="member member--a" role="img" aria-label="Member photo"></span>
      <span class="member member--b" role="img" aria-label="Member photo"></span>
    </div>
  </article>

  <article class="list-card list-card--party">
    <div class="list-scene" role="img" aria-label="Illustration of a party table with drinks and string lights"></div>
    <h2 class="list-title">Party</h2>
    <span class="list-count">4 items</span>
    <div class="list-members">
      <span class="member member--a" role="img" aria-label="Member photo"></span>
      <span class="member member--c" role="img" aria-label="Member photo"></span>
      <span class="member member--d" role="img" aria-label="Member photo"></span>
    </div>
  </article>

  <article class="list-card list-card--grocery">
    <div class="list-scene" role="img" aria-label="Illustration of a grocery store with a shopping basket"></div>
    <h2 class="list-title">Grocery Store</h2>
    <span class="list-count">3 items</span>
    <div class="list-members">
      <span class="member member--a" role="img" aria-label="Member photo"></span>
    </div>
  </article>

  <div class="create-list">
    <span class="create-plus">+</span>
    <span class="create-label">Create list</span>
  </div>
</nav>
</body>
</html>
```